Business Card Design

We are a commercial real estate brokerage in San Francisco, leasing office buildings downtown.
I would like a clean, elegant look. Simple but powerful .

Industry/Entity Type

Business

Contact Information for Business Card

Colin Farrow
lic# 07281549
415.555.0172
colin@tarvo-commercial.example
tarvo-commercial.example

```html
<!DOCTYPE html>
<html lang="en">
<head>
<meta charset="utf-8">
<title>Tarvo Commercial – Business Card</title>
<link href="https://fonts.googleapis.com/css2?family=Jost:wght@400;500;600&display=swap" rel="stylesheet">
<style>
  :root {
    --backdrop: #1c1c1d;
    --card-white: #ffffff;
    --slate-blue: #7486a4;
    --charcoal: #2e2e30;
    --charcoal-deep: #242426;
    --rule: #4a4a4d;
    --text-light: #f2f2f2;
    --text-soft: #dfe4ec;
    --brand-ink: #6f82a1;
  }
  * { margin: 0; padding: 0; box-sizing: border-box; }
  html, body {
    width: 1200px; height: 800px; overflow: hidden;
    background: var(--backdrop);
    font-family: "Jost", "Helvetica Neue", Arial, sans-serif;
  }
  .stage { position: relative; width: 1200px; height: 800px; }
  .card {
    position: absolute; left: 180px; top: 160px;
    width: 840px; height: 480px;
    background: var(--card-white);
    box-shadow: 0 18px 40px rgba(0,0,0,.45);
    overflow: hidden;
  }
  .card-shapes { position: absolute; inset: 0; }
  .holder { position: absolute; left: 58px; top: 44px; color: var(--text-light); }
  .holder-name { font-size: 29px; font-weight: 500; letter-spacing: 1.5px; line-height: 1.1; }
  .holder-licence { font-size: 22px; font-weight: 400; color: var(--text-soft); letter-spacing: .5px; }
  .contact-list { position: absolute; left: 58px; top: 140px; width: 350px; list-style: none; }
  .contact-item {
    display: flex; align-items: center; gap: 20px;
    height: 66px; color: var(--text-light);
    font-size: 18px; letter-spacing: .4px;
    border-bottom: 1.5px solid var(--rule);
    white-space: nowrap;
  }
  .contact-item:last-child { border-bottom: none; }
  .contact-icon { width: 24px; height: 24px; flex: none; }
  .brand {
    position: absolute; left: 584px; top: 214px;
    display: flex; align-items: center; gap: 14px;
    color: var(--brand-ink); font-weight: 600;
  }
  .brand-mark { width: 28px; height: 28px; background: var(--brand-ink); flex: none; }
  .brand-name {
    font-size: 26px; line-height: 1.05; letter-spacing: 1px;
    text-transform: uppercase; white-space: nowrap;
  }
  .brand-name span { display: block; }
</style>
</head>
<body>
<main class="stage">
  <section class="card" aria-label="Business card for Colin Farrow, Tarvo Commercial">
    <svg class="card-shapes" viewBox="0 0 840 480" aria-hidden="true">
      <path d="M0 30 H392 Q412 30 424 46 L458 125 H0 Z" fill="var(--slate-blue)"/>
      <path d="M0 125 H458 L560 360 H0 Z" fill="var(--charcoal)"/>
      <path d="M560 360 L570 352 H840 V440 H610 Q596 440 590 430 Z" fill="var(--slate-blue)"/>
      <path d="M610 440 H840 V470 H634 Z" fill="var(--charcoal-deep)"/>
    </svg>

    <div class="holder">
      <p class="holder-name">COLIN FARROW</p>
      <p class="holder-licence">lic# 07281549</p>
    </div>

    <ul class="contact-list">
      <li class="contact-item">
        <svg class="contact-icon" viewBox="0 0 24 24" fill="none" stroke="currentColor" stroke-width="1.6" aria-hidden="true">
          <circle cx="12" cy="12" r="9"/><ellipse cx="12" cy="12" rx="4" ry="9"/><path d="M3 12h18M5 7h14M5 17h14"/>
        </svg>
        <span>tarvo-commercial.example</span>
      </li>
      <li class="contact-item">
        <svg class="contact-icon" viewBox="0 0 24 24" fill="none" stroke="currentColor" stroke-width="1.6" aria-hidden="true">
          <circle cx="12" cy="12" r="10"/>
          <path d="M8.5 7.5l1.8-.4 1 2.6-1.2 1c.6 1.3 1.6 2.3 2.9 2.9l1-1.2 2.6 1-.4 1.8c-3.8.3-7.9-3.8-7.7-7.7z" fill="currentColor" stroke="none"/>
        </svg>
        <span>415.555.0172</span>
      </li>
      <li class="contact-item">
        <svg class="contact-icon" viewBox="0 0 24 24" aria-hidden="true">
          <path d="M4 7h16v11H4z" fill="currentColor"/>
          <path d="M4 7l8 6 8-6" fill="none" stroke="var(--charcoal)" stroke-width="1.6"/>
        </svg>
        <span>colin@tarvo-commercial.example</span>
      </li>
    </ul>

    <div class="brand">
      <div class="brand-mark"></div>
      <p class="brand-name"><span>Tarvo</span><span>Commercial</span></p>
    </div>
  </section>
</main>
</body>
</html>
```